Promotional Flyer/Email Design - Cabling services for Broadcast and Audio Visual

We need a promotional flyer/email design to help launch our company, Velcor Lane. We provide cabling services for Broadcast Television and Audio Visual systems. Recent projects include major television events such as the Harrowmere Racquet Classic and Audio Visual/Entertainment systems for wealthy clients in their homes and on-board super yachts.

The flyer will be printed as single sided A5 and also be sent out in the body of a promotional email. It should feature the company logo along with a complementary colour scheme. It should have a clean finish with images that show the type of work we do (cabling and equipment installation) or the setting for these systems (tv studio, super yacht, cinema room, meeting room with projector etc.)

Services we offer are:

Broadcast/AV system design
On-site installation
Rack building
Pre-fabricated cable looms
Fibre optic installation

About the company:

Velcor Lane provide cabling services for Broadcast Television and Audio Visual systems. With over 15 years experience working in these industries we can help with every aspect of design, project managment, installation and maintenance. Our projects range from fibre optic cabling at major sports events to installing and commisioning bespoke control systems on some of the worlds largest super yachts.

Contact details:

To get a quote or discuss your project contact us now
Telephone: TBC
Email: info@velcor-lane.com
Website: www.velcor-lane.com
Address: TBC

Other information:

The company is based in London, UK. Our projects often take place in other countries with work taking place accross Europe and beyond.

We have a London based workshop for rack building and cable pre-fabrication.

Our website is www.velcor-lane.com

Images:

Images attached can be editted for use on the flyer or have ideas taken from them. Only the company logo is required to feature on the final design.

Target Market(s)

Business to business

Industry/Entity Type

It Company

Font styles to use
Sans Serif

Requirements
Must have
• Company logo
• List of services
• Contact details
Nice to have
• Image of cabling, home cinema room, super yacht, luxury home, outside broadcast truck, fibre optic equipment or cabling.

```html
<!DOCTYPE html>
<html lang="en">
<head>
<meta charset="utf-8">
<title>Velcor Lane – Broadcast &amp; AV System Installation</title>
<link rel="stylesheet" href="https://fonts.googleapis.com/css2?family=Montserrat:wght@400;500;600;700;800&family=Source+Sans+3:wght@400&display=swap">
<style>
  :root {
    --ink: #2a2a2c;
    --dark: #2b2b2d;
    --blue: #1a9ad6;
    --deep-blue: #1f5fae;
    --red: #d0183d;
    --paper: #f1f1f2;
    --grey: #cfd0d2;
    --white: #ffffff;
  }
  * { margin: 0; padding: 0; box-sizing: border-box; }
  html, body { width: 950px; height: 1200px; overflow: hidden; background: #e6e6e6; }
  .flyer {
    position: relative; width: 950px; height: 1200px; overflow: hidden;
    background: var(--paper); font-family: "Montserrat", sans-serif; color: var(--ink);
  }
  .hero-art { position: absolute; left: 0; top: 0; width: 950px; height: 600px; }
  .brand {
    position: absolute; left: 44px; top: 130px;
    font-family: "Montserrat", sans-serif; font-weight: 600; font-size: 40px;
    color: var(--white); letter-spacing: -0.5px; display: flex; align-items: center; gap: 12px;
  }
  .brand-mark { width: 18px; height: 18px; border-radius: 50%; background: var(--red); }
  .headline-bar { position: absolute; left: 4px; top: 198px; width: 14px; height: 130px; background: var(--blue); }
  .headline {
    position: absolute; left: 44px; top: 196px;
    font-weight: 800; font-size: 42px; line-height: 45px; color: var(--white); letter-spacing: 0.3px;
  }
  .headline .accent { color: var(--blue); }
  .tagline {
    position: absolute; left: 48px; top: 352px; width: 300px;
    font-family: "Source Sans 3", sans-serif; font-size: 18px; line-height: 21px; color: var(--white);
  }
  .section-title { position: absolute; left: 48px; font-size: 28px; font-weight: 500; color: #4a4a4c; }
  .section-title strong { color: var(--blue); font-weight: 800; }
  .about-title { top: 614px; }
  .about-text {
    position: absolute; left: 48px; top: 658px; width: 860px;
    font-size: 15.6px; line-height: 20.5px; color: var(--ink); text-align: justify;
  }
  .services-title { top: 762px; }
  .service {
    position: absolute; width: 240px; text-align: center;
    font-size: 18px; font-weight: 700; line-height: 21px; color: #4a4a4c; text-transform: uppercase;
  }
  .service svg { display: block; margin: 0 auto 6px; width: 46px; height: 46px; }
  .footer-panel { position: absolute; left: 0; top: 1027px; width: 950px; height: 173px; }
  .footer-brand {
    position: absolute; left: 48px; top: 1090px;
    font-size: 32px; font-weight: 600; color: var(--ink); display: flex; align-items: center; gap: 10px;
  }
  .footer-brand .brand-mark { width: 14px; height: 14px; }
  .footer-links {
    position: absolute; left: 50px; top: 1140px;
    font-size: 13px; font-weight: 700; line-height: 17px; color: var(--red);
  }
  .cta {
    position: absolute; left: 322px; top: 1044px;
    font-size: 17.5px; font-weight: 600; line-height: 22px; color: var(--red);
  }
  .phone { position: absolute; left: 320px; top: 1092px; font-size: 32px; font-weight: 700; color: var(--white); }
  .address {
    position: absolute; left: 322px; top: 1145px; font-size: 15.5px; font-weight: 500; color: var(--white);
    display: flex; align-items: center; gap: 8px;
  }
  .divider { position: absolute; left: 604px; top: 1044px; width: 1px; height: 124px; background: var(--red); }
  .company-info {
    position: absolute; left: 618px; top: 1040px; width: 300px;
    font-size: 14.2px; line-height: 18px; color: var(--white);
  }
  .company-info p + p { margin-top: 5px; }
</style>
</head>
<body>
<div class="flyer">

  <svg class="hero-art" viewBox="0 0 950 600" xmlns="http://www.w3.org/2000/svg">
    <defs>
      <linearGradient id="hero-dark" x1="0" y1="0" x2="1" y2="1">
        <stop offset="0" stop-color="#2a2a2c"/>
        <stop offset="1" stop-color="#3c3d40"/>
      </linearGradient>
      <linearGradient id="city" x1="0" y1="0" x2="0" y2="1">
        <stop offset="0" stop-color="#e4e4e6"/>
        <stop offset="1" stop-color="#b9babd"/>
      </linearGradient>
      <linearGradient id="room" x1="0" y1="0" x2="1" y2="1">
        <stop offset="0" stop-color="#8a7b66"/>
        <stop offset="0.5" stop-color="#5e5245"/>
        <stop offset="1" stop-color="#3a3129"/>
      </linearGradient>
      <linearGradient id="rack" x1="0" y1="0" x2="0" y2="1">
        <stop offset="0" stop-color="#3f4a45"/>
        <stop offset="1" stop-color="#232826"/>
      </linearGradient>
      <linearGradient id="panel" x1="0" y1="0" x2="1" y2="0">
        <stop offset="0" stop-color="#b8b3a6"/>
        <stop offset="1" stop-color="#e6e2d8"/>
      </linearGradient>
    </defs>
    <!-- dark backdrop -->
    <rect role="img" aria-label="Dim photo of a technician working on a cable rack" width="950" height="600" fill="url(#hero-dark)"/>
    <!-- light city backdrop on the right -->
    <path role="img" aria-label="Faded city skyline" d="M950 100 C 840 220 700 420 560 600 L950 600 Z" fill="url(#city)"/>
    <!-- paper curve -->
    <path d="M0 590 C 250 520 560 560 950 600 L950 600 L0 600 Z" fill="var(--paper)"/>
    <!-- blue and red swoosh bands -->
    <path d="M0 470 C 120 455 240 470 330 520 L330 560 C 230 515 110 505 0 520 Z" fill="var(--deep-blue)"/>
    <path d="M0 520 C 110 505 230 515 330 560 L330 590 C 220 560 100 570 0 585 Z" fill="var(--red)"/>
    <!-- large photo circle -->
    <circle cx="672" cy="262" r="240" fill="#f3f3f3"/>
    <circle role="img" aria-label="Photo of a luxury living room with wall mounted television" cx="672" cy="262" r="226" fill="url(#room)"/>
    <!-- rack photo circle -->
    <circle cx="460" cy="466" r="126" fill="var(--red)"/>
    <circle role="img" aria-label="Photo of an equipment rack with neatly dressed cables" cx="460" cy="466" r="118" fill="url(#rack)"/>
    <!-- panel photo circle -->
    <circle cx="244" cy="514" r="92" fill="#4f86c9"/>
    <circle role="img" aria-label="Photo of a wall mounted cable distribution panel" cx="244" cy="514" r="84" fill="url(#panel)"/>
  </svg>

  <div class="brand"><span class="brand-mark"></span>Velcor Lane</div>

  <div class="headline-bar"></div>
  <h1 class="headline">BROADCAST &amp;<br><span class="accent">AV SYSTEM</span><br>INSTALLATION</h1>
  <p class="tagline">Velcor Lane provide cabling services for the Broadcast and Audio Visual industries.</p>

  <h2 class="section-title about-title"><strong>ABOUT</strong> US</h2>
  <p class="about-text">Velcor Lane provide cabling services for Broadcast Television and Audio Visual systems. With over 15 years experience working in these industries we can help with every aspect of design, project managment, installation and maintenance. Our projects range from fibre optic cabling at major sports events to installing and commisioning bespoke control systems on some of the worlds largest super yachts.</p>

  <h2 class="section-title services-title"><strong>SERVICES</strong> WE OFFER</h2>

  <div class="service" style="left:52px; top:826px;">
    <svg viewBox="0 0 48 48" fill="none" stroke="var(--red)" stroke-width="3.5" stroke-linejoin="round">
      <path d="M10 8 L40 38 L34 44 L4 14 Z"/><path d="M36 6 L42 12 L14 40 L6 42 L8 34 Z"/>
    </svg>
    Broadcast/<br>AV System Design
  </div>
  <div class="service" style="left:394px; top:826px;">
    <svg viewBox="0 0 48 48" fill="none" stroke="var(--red)" stroke-width="4" stroke-linecap="round">
      <path d="M30 6 a10 10 0 0 0 8 14 L14 42 L6 34 L28 12 a10 10 0 0 1 2 -6"/><path d="M8 8 L40 40"/>
    </svg>
    On-site<br>Installation
  </div>
  <div class="service" style="left:675px; top:828px;">
    <svg viewBox="0 0 48 48" fill="none" stroke="var(--red)" stroke-width="3.5">
      <rect x="6" y="4" width="36" height="9" rx="2"/><rect x="6" y="15" width="36" height="9" rx="2"/>
      <rect x="6" y="26" width="36" height="9" rx="2"/><rect x="6" y="37" width="36" height="8" rx="2"/>
    </svg>
    Rack<br>Building
  </div>
  <div class="service" style="left:262px; top:922px;">
    <svg viewBox="0 0 48 48" fill="none" stroke="var(--red)" stroke-width="5" stroke-linecap="round">
      <path d="M6 16 H18 V40 H30 V10 H42"/>
    </svg>
    Pre-fabricated<br>Cable Looms
  </div>
  <div class="service" style="left:509px; top:922px;">
    <svg viewBox="0 0 48 48" fill="none" stroke="var(--red)" stroke-width="3" stroke-linecap="round">
      <path d="M8 42 L22 26 M22 26 L22 8 M22 26 L40 22 M22 26 L36 10 M22 26 L36 38"/>
      <circle cx="22" cy="6" r="3"/><circle cx="42" cy="22" r="3"/><circle cx="38" cy="8" r="3"/><circle cx="38" cy="40" r="3"/>
    </svg>
    Fibre Optic<br>Installation
  </div>

  <svg class="footer-panel" viewBox="0 0 950 173" xmlns="http://www.w3.org/2000/svg">
    <rect width="950" height="173" fill="var(--white)"/>
    <path d="M268 0 H950 V160 H298 Z" fill="var(--dark)"/>
    <rect x="298" y="160" width="652" height="13" fill="var(--deep-blue)"/>
  </svg>

  <div class="footer-brand"><span class="brand-mark"></span>Velcor Lane</div>
  <div class="footer-links">INFO@VELCOR-LANE.COM<br>WWW.VELCOR-LANE.COM</div>

  <p class="cta">To get a quote or discuss<br>your project contact us now</p>
  <p class="phone">00-210-555-0147</p>
  <p class="address">
    <svg width="16" height="18" viewBox="0 0 16 18"><path d="M8 0 a7 7 0 0 1 7 7 c0 5 -7 11 -7 11 s-7 -6 -7 -11 a7 7 0 0 1 7 -7 Z" fill="var(--red)"/><circle cx="8" cy="7" r="2.6" fill="var(--dark)"/></svg>
    Address Goes Here
  </p>
  <div class="divider"></div>
  <div class="company-info">
    <p>The company is based in London, UK. Our projects often take place in other countries with work taking place accross Europe and beyond.</p>
    <p>We have a London based workshop for rack building and cable pre-fab-rication.</p>
  </div>

</div>
</body>
</html>
```